Full color cover for Chamber's Membership Menu

I need a cover, 8 1/2" x 11" for our Chamber of Commerce Membership Menu. Is should have our logo and the words, Membership Menu on it. That's all that is necessary but it can include one or more of the other photos (maybe a college?) that I added, though they are not required. Our logo colors should be used: 37-170-226, 58-181-74, 40-56-144, 247-148-29, 189-190-192.

Target Market(s)

Business owners and managers

Industry/Entity Type

Business Development

Font styles to use
Serif

Colors
0054AA
0677BA
7BADD7
CADEEF
E8F1F8
00AB8E
00BBA5
67D7C9
C6EFE9
E9F9F6
F0912C
F2A743
F7CA91
FBE8D2
FDF5EE

Requirements
Must have
• Our logo and the words Membership Menu
Nice to have
• An attractive business-like feel. It can be very simple.

```html
<!DOCTYPE html>
<html lang="en">
<head>
<meta charset="utf-8">
<title>Membership Menu – Cover</title>
<link href="https://fonts.googleapis.com/css2?family=Raleway:wght@200;600&display=swap" rel="stylesheet">
<style>
  :root {
    --stage: #d9d9db;
    --paper: #f4f5f7;
    --paper-shade: #e6e7ea;
    --ink-blue: #3b48a6;
    --logo-blue: #28388f;
    --logo-dot: #25aae2;
    --band-top: #5a8fd6;
    --band-bottom: #3c3f9c;
    --facet-line: rgba(255, 255, 255, 0.9);
    --facet-shade: rgba(200, 203, 210, 0.35);
    --photo-gap: #ffffff;
  }
  * { margin: 0; padding: 0; box-sizing: border-box; }
  html, body {
    width: 1200px; height: 1200px; overflow: hidden;
    background: var(--stage);
  }
  .cover {
    position: absolute; left: 120px; top: 120px;
    width: 960px; height: 960px;
    background: linear-gradient(160deg, var(--paper) 0%, #ffffff 45%, var(--paper-shade) 100%);
    box-shadow: 0 12px 30px rgba(0,0,0,0.12);
    overflow: hidden;
  }
  .facets { position: absolute; inset: 0; }
  .brand {
    position: absolute; left: 150px; top: 130px;
    display: flex; align-items: center; gap: 14px;
    font-family: "Raleway", sans-serif; font-weight: 600;
    color: var(--logo-blue);
  }
  .brand-dot {
    width: 54px; height: 54px; border-radius: 50%;
    background: var(--logo-dot);
  }
  .brand-name { font-size: 22px; line-height: 1.15; letter-spacing: 1px; text-transform: uppercase; }
  .brand-name small { display: block; font-size: 13px; letter-spacing: 3px; }
  .title {
    position: absolute; left: 150px; top: 225px;
    font-family: "Raleway", sans-serif; font-weight: 200;
    font-size: 88px; line-height: 1.02; letter-spacing: 2px;
    color: var(--ink-blue); text-transform: uppercase;
  }
  .accent-band {
    position: absolute; left: 830px; top: 325px; width: 130px; height: 250px;
    background: linear-gradient(180deg, var(--band-top), var(--band-bottom));
  }
  .photo {
    position: absolute; border: 5px solid var(--photo-gap);
  }
  .photo-reception-a { left: 0; top: 500px; width: 335px; height: 120px; background: linear-gradient(135deg, #6b5440, #3a2c22); }
  .photo-reception-b { left: 0; top: 620px; width: 335px; height: 125px; background: linear-gradient(135deg, #5a3f33, #2c2320); }
  .photo-ribbon-a { left: 335px; top: 430px; width: 245px; height: 120px; background: linear-gradient(135deg, #a9a2b0, #6d5f86); }
  .photo-welcome { left: 335px; top: 550px; width: 245px; height: 125px; background: linear-gradient(135deg, #e9e5df, #b88b6f); }
  .photo-ribbon-b { left: 580px; top: 345px; width: 245px; height: 115px; background: linear-gradient(135deg, #8c8a7a, #54627a); }
  .photo-team { left: 580px; top: 460px; width: 245px; height: 120px; background: linear-gradient(135deg, #b89a78, #3e342e); }
</style>
</head>
<body>
  <main class="cover">
    <svg class="facets" width="960" height="960" viewBox="0 0 960 960" aria-hidden="true">
      <polygon points="0,960 420,720 960,800 960,960" fill="var(--facet-shade)"/>
      <polygon points="520,0 960,0 960,260" fill="var(--facet-shade)"/>
      <g stroke="var(--facet-line)" stroke-width="2" fill="none">
        <line x1="0" y1="960" x2="420" y2="720"/>
        <line x1="420" y1="720" x2="960" y2="800"/>
        <line x1="640" y1="960" x2="880" y2="580"/>
        <line x1="300" y1="760" x2="960" y2="940"/>
        <line x1="520" y1="0" x2="960" y2="260"/>
        <line x1="700" y1="0" x2="560" y2="120"/>
        <line x1="760" y1="700" x2="960" y2="640"/>
      </g>
    </svg>

    <div class="brand">
      <span class="brand-dot"></span>
      <span class="brand-name">Harborview Chamber<small>of Commerce &amp; Tourism</small></span>
    </div>

    <h1 class="title">Membership<br>Menu</h1>

    <div class="accent-band"></div>

    <div class="photo photo-reception-a" role="img" aria-label="Members mingling at an evening chamber reception"></div>
    <div class="photo photo-reception-b" role="img" aria-label="Group of members posing together at a networking event"></div>
    <div class="photo photo-ribbon-a" role="img" aria-label="Ribbon cutting outside a newly opened local business"></div>
    <div class="photo photo-welcome" role="img" aria-label="Two members smiling in front of the chamber office sign"></div>
    <div class="photo photo-ribbon-b" role="img" aria-label="Crowd gathered for a ribbon cutting inside a shop"></div>
    <div class="photo photo-team" role="img" aria-label="Restaurant staff in aprons standing together"></div>
  </main>
</body>
</html>
```